Allied Health team of Physiotherapists & Occupational Therapists seek a business card design

We have our new logo, we now need our new business cards and stationary. Blossom: Lymphoedema & Women's Clinic is seeking a generic card design to represent our whole team and individual cards for each therapist that incorporates our new logo to communicate our holistic approach that is calming, nuturing, supportive and welcoming.
Our Physiotherapists and Occupational Therapists assess, treat and provide education for people who are at risk of or who have lymphoedema. This is often as a result of treatment for cancer. We provide pre-operative and post-operative management and cancer rehabilitation in our Pilates studio. Our team also consists of Physiotherapists who have a strong interest in pelvic floor and continence management for both men and women.

Target Market(s)

Mainly women health conscious

Industry/Entity Type

Allied Health: Physiotherapy / Occupational Therapy

Contact Information for Business Card

Address: 14 Calloway Ave Elmsworth 3271 Phone: 84317560 fax: 8431 7564 Email: info@blossomcarepartners.com.au Website: blossomcarepartners.com.au Facebook address: facebook.com/BlossomLymphoedemaAndWomensCareCentre. Room to write appointments. Individual cards need to have name, office email and individual email and professional details

Requirements
Must have
• Logo as per uploaded documents

```html
<!DOCTYPE html>
<html lang="en">
<head>
<meta charset="utf-8">
<title>Blossom – Business Card</title>
<link href="https://fonts.googleapis.com/css2?family=Roboto:wght@300;400;700&display=swap" rel="stylesheet">
<style>
  :root {
    --indigo: #2e3092;
    --indigo-deep: #302c66;
    --peach: #f9ad7c;
    --ink: #111111;
    --ink-soft: #333333;
    --paper: #ffffff;
    --backdrop: #f2f2f7;
  }
  * { margin: 0; padding: 0; box-sizing: border-box; }
  html, body {
    width: 1200px; height: 1200px; overflow: hidden;
    background: var(--backdrop);
    font-family: "Roboto", sans-serif;
  }
  .canvas { position: relative; width: 1200px; height: 1200px; }

  .card { position: absolute; left: 285px; width: 630px; overflow: hidden; }

  /* Front */
  .card-front { top: 176px; height: 359px; background: var(--indigo); }
  .brand-mark {
    position: absolute; left: 0; right: 0; top: 128px;
    display: flex; flex-direction: column; align-items: center; gap: 6px;
    color: var(--peach); font-weight: 400; text-align: center;
  }
  .brand-name { font-size: 30px; line-height: 1; }
  .brand-sub { font-size: 12px; letter-spacing: 1.5px; text-transform: uppercase; }
  .web-band {
    position: absolute; left: 0; right: 0; top: 269px; height: 58px;
    background: var(--indigo-deep);
    display: flex; align-items: center; justify-content: center; gap: 9px;
    color: var(--peach); font-size: 17.5px; font-weight: 400;
  }
  .web-band svg { width: 22px; height: 22px; }

  /* Back */
  .card-back { top: 602px; height: 379px; background: var(--paper); }
  .card-back .shapes { position: absolute; inset: 0; width: 630px; height: 379px; }
  .back-brand {
    position: absolute; left: 20px; width: 160px; top: 160px;
    color: var(--peach); font-weight: 400; text-align: center;
    font-size: 13px; line-height: 1.35;
  }
  .back-brand .brand-name { font-size: 24px; display: block; margin-bottom: 4px; }

  .person { position: absolute; right: 55px; top: 50px; text-align: right; }
  .person-name { font-size: 27px; font-weight: 700; color: var(--ink); line-height: 1.1; margin-bottom: 5px; }
  .person-quals { font-size: 13.5px; font-weight: 300; color: var(--ink-soft); line-height: 17px; }

  .contacts {
    position: absolute; left: 288px; top: 245px;
    font-size: 16.5px; color: var(--ink); font-weight: 400;
  }
  .contact-row { display: flex; align-items: center; height: 29px; }
  .contact-item { display: flex; align-items: center; gap: 5px; margin-right: 16px; }
  .icon {
    width: 22px; height: 22px; border-radius: 50%; background: var(--indigo);
    display: flex; align-items: center; justify-content: center; flex: none;
  }
  .icon svg { width: 13px; height: 13px; }
</style>
</head>
<body>
<div class="canvas">

  <section class="card card-front">
    <div class="brand-mark">
      <span class="brand-name">Blossom</span>
      <span class="brand-sub">Lymphoedema &amp; Women's Clinic</span>
    </div>
    <div class="web-band">
      <svg viewBox="0 0 24 24" fill="none" stroke="#f9ad7c" stroke-width="1.6">
        <circle cx="12" cy="12" r="10"/>
        <ellipse cx="12" cy="12" rx="4.5" ry="10"/>
        <line x1="2" y1="12" x2="22" y2="12"/>
        <path d="M4 7h16M4 17h16"/>
      </svg>
      <span>blossomcarepartners.com.au</span>
    </div>
  </section>

  <section class="card card-back">
    <svg class="shapes" viewBox="0 0 630 379">
      <circle cx="32" cy="189" r="189" fill="#f9ad7c"/>
      <circle cx="12" cy="189" r="189" fill="#2e3092"/>
      <circle cx="810" cy="189" r="222" fill="#f9ad7c"/>
      <circle cx="818" cy="189" r="222" fill="#2e3092"/>
    </svg>

    <div class="back-brand">
      <span class="brand-name">Blossom</span>
      Lymphoedema &amp;<br>Women's Clinic
    </div>

    <div class="person">
      <h1 class="person-name">Maren Holloway</h1>
      <p class="person-quals">B. Physio (Hons), B.Sc.(Exercise Science/Anatomy)</p>
      <p class="person-quals">Post Grad Certif. Oncology Rehab</p>
      <p class="person-quals">Grad Dip. Lymphatic Therapy &amp; Women's Health Practice</p>
    </div>

    <div class="contacts">
      <div class="contact-row">
        <span class="contact-item">
          <span class="icon"><svg viewBox="0 0 16 16" fill="none" stroke="#f9ad7c" stroke-width="1.3"><path d="M2 6c0-2 2-3 6-3s6 1 6 3l-2 1-1-2H5L4 7z"/><rect x="4" y="8" width="8" height="5" rx="1"/></svg></span>
          84317560
        </span>
        <span class="contact-item">
          <span class="icon"><svg viewBox="0 0 16 16" fill="none" stroke="#f9ad7c" stroke-width="1.3"><rect x="3" y="6" width="10" height="7" rx="1"/><path d="M5 6V2h6v4M5 9h6M5 11h6"/></svg></span>
          8431 7564
        </span>
      </div>
      <div class="contact-row">
        <span class="contact-item">
          <span class="icon"><svg viewBox="0 0 16 16" fill="none" stroke="#f9ad7c" stroke-width="1.3"><rect x="2" y="4" width="12" height="9" rx="1"/><path d="M2 5l6 4 6-4"/></svg></span>
          info@blossomcarepartners.com.au
        </span>
      </div>
      <div class="contact-row">
        <span class="contact-item">
          <span class="icon"><svg viewBox="0 0 16 16" fill="none" stroke="#f9ad7c" stroke-width="1.3"><path d="M8 15s5-5 5-8.5a5 5 0 0 0-10 0C3 10 8 15 8 15z"/><circle cx="8" cy="6.5" r="1.8"/></svg></span>
          14 Calloway Ave, Elmsworth 3271
        </span>
      </div>
    </div>
  </section>

</div>
</body>
</html>
```